Business Card Design

We need a business card designed for our new company. Prefer a black card with white logo & writing.

Contact Information for Business Card

Dale Pickett, address: 7-4417 Larchmere Avenue, Abbotsford, BC, V3K 2R9, Office Phone: 604-555-0172, Cell: 604-555-0138, Email: dale@kelsoncoatworks.ca

Colors

Designer to choose only greyscale colors for use in the design.

```html
<!DOCTYPE html>
<html lang="en">
<head>
<meta charset="utf-8">
<title>Kelson Coatworks – Business Card</title>
<link rel="stylesheet" href="https://fonts.googleapis.com/css2?family=Poiret+One&display=swap">
<style>
  :root {
    --page: #ffffff;
    --card: #201c1b;
    --ink: #ffffff;
    --band: #4d4a49;
    --line: #ffffff;
  }
  * { margin: 0; padding: 0; box-sizing: border-box; }
  html, body {
    width: 1200px;
    height: 999px;
    overflow: hidden;
    background: var(--page);
  }
  body {
    position: relative;
    font-family: "Poiret One", sans-serif;
    color: var(--ink);
  }
  .card {
    position: absolute;
    left: 208px;
    width: 728px;
    height: 405px;
    background: var(--card);
    overflow: hidden;
  }
  .card--front { top: 52px; }
  .card--back { top: 516px; }

  .wordmark {
    position: absolute;
    text-align: center;
    text-transform: uppercase;
    font-weight: 400;
    color: var(--ink);
    line-height: 1;
  }
  .wordmark__top { display: block; }
  .wordmark__bottom { display: block; }

  .card--front .wordmark {
    left: 87px;
    top: 64px;
    width: 200px;
  }
  .card--front .wordmark__top { font-size: 34px; letter-spacing: 3px; }
  .card--front .wordmark__bottom { font-size: 17px; letter-spacing: 5px; margin-top: 6px; }

  .holder-name {
    position: absolute;
    left: 95px;
    top: 218px;
    font-size: 29px;
    letter-spacing: 2px;
    text-transform: uppercase;
  }
  .divider {
    position: absolute;
    left: 339px;
    top: 137px;
    width: 3px;
    height: 167px;
    background: var(--line);
  }
  .contact {
    position: absolute;
    left: 369px;
    top: 143px;
    list-style: none;
    font-size: 19px;
    letter-spacing: 1.3px;
    text-transform: uppercase;
    line-height: 26px;
  }
  .contact li { margin-bottom: 11px; }
  .contact li.contact__address { margin-bottom: 11px; }

  .band-rule {
    position: absolute;
    left: 0;
    top: 359px;
    width: 100%;
    height: 5px;
    background: var(--line);
  }
  .band {
    position: absolute;
    left: 0;
    top: 364px;
    width: 100%;
    height: 41px;
    background: var(--band);
  }

  .card--back .wordmark {
    left: 0;
    top: 142px;
    width: 100%;
  }
  .card--back .wordmark__top { font-size: 76px; letter-spacing: 6px; }
  .card--back .wordmark__bottom { font-size: 30px; letter-spacing: 10px; margin-top: 14px; }
</style>
</head>
<body>
  <section class="card card--front" aria-label="Card front">
    <div class="wordmark">
      <span class="wordmark__top">Kelson</span>
      <span class="wordmark__bottom">Coatworks</span>
    </div>
    <p class="holder-name">Dale Pickett</p>
    <div class="divider"></div>
    <ul class="contact">
      <li class="contact__address">7-4417 Larchmere Avenue,<br>Abbotsford, BC, V3K 2R9</li>
      <li>604-555-0172</li>
      <li>604-555-0138</li>
      <li>dale@kelsoncoatworks.ca</li>
    </ul>
    <div class="band-rule"></div>
    <div class="band"></div>
  </section>

  <section class="card card--back" aria-label="Card back">
    <div class="wordmark">
      <span class="wordmark__top">Kelson</span>
      <span class="wordmark__bottom">Coatworks</span>
    </div>
  </section>
</body>
</html>
```